Vemtra Group: Business Card for a high end technology company

We need a cool new design for our business cards using our cloud logo. We are a technology consulting business. We pride ourselves on be the best of the best. We mainly focus on cloud solutions and managed services. We need a business card that sets us apart from the other technology companies in the area and allows us to stand out.

Target Market(s)

Technology departments, CIO, CEOs, and Information Technology Staff.

Industry/Entity Type

Information Technology

Contact Information for Business Card

Must have the logo and our name.
Must have employee name, email address, office phone, cell phone and website.
Need to have all info on one side a cool design on backside.

Font styles to use
Serif
Sans Serif

Requirements
Must have
• Must have the logo and our name.
• Must have employee name, email address, office phone, cell phone and website.
• Need to have all info on one side a cool design on back side.
• Must be a crisp clean design, not too busy or confusing.

```html
<!DOCTYPE html>
<html lang="en">
<head>
<meta charset="utf-8">
<title>Vemtra Group – Business Card</title>
<link rel="stylesheet" href="https://fonts.googleapis.com/css2?family=Lato:wght@300;400;700&display=swap">
<style>
  :root {
    --page-bg: #e9eaec;
    --card-bg: #ffffff;
    --ink: #2b2b2e;
    --ink-soft: #4a4a4f;
    --brand-blue: #3d9fe0;
    --brand-deep: #3a6fcf;
  }
  * { margin: 0; padding: 0; box-sizing: border-box; }
  html, body {
    width: 1200px; height: 900px; overflow: hidden;
    background: var(--page-bg);
    font-family: "Lato", sans-serif;
    color: var(--ink);
  }
  .card {
    position: absolute;
    left: 318px;
    width: 560px; height: 320px;
    background: var(--card-bg);
    box-shadow: 0 2px 8px rgba(0,0,0,0.12);
  }
  .card--front { top: 91px; }
  .card--back { top: 482px; }

  /* Front: brand block */
  .brand-front {
    position: absolute; left: 36px; top: 84px; width: 204px;
    text-align: center;
  }
  .brand-dot {
    display: block; margin: 0 auto 14px;
    width: 66px; height: 66px; border-radius: 50%;
    background: var(--brand-blue);
  }
  .brand-name {
    font-weight: 400; font-size: 32px; line-height: 1;
    color: var(--ink); white-space: nowrap; letter-spacing: -0.3px;
  }
  .brand-url {
    margin-top: 7px; font-size: 10px; font-weight: 700;
    letter-spacing: 0.6px; color: var(--ink);
  }

  /* Front: contact block */
  .contact { position: absolute; left: 298px; top: 108px; }
  .contact__name { font-size: 22px; font-weight: 700; color: var(--ink); margin-bottom: 8px; letter-spacing: -0.2px; }
  .contact__row {
    display: flex; align-items: flex-start; gap: 7px;
    font-size: 14px; font-weight: 300; color: var(--ink-soft); line-height: 18px;
  }
  .contact__row + .contact__row { margin-top: 1px; }
  .contact__icon { width: 12px; height: 14px; flex: none; margin-top: 2px; fill: var(--brand-blue); }
  .contact__row--plain { padding-left: 19px; }

  .front-rule {
    position: absolute; left: 11px; right: 11px; top: 275px;
    height: 2.5px; background: var(--brand-blue);
  }

  /* Back */
  .brand-back {
    position: absolute; left: 0; right: 0; top: 58px; text-align: center;
  }
  .brand-back .brand-dot { width: 96px; height: 96px; margin-bottom: 22px; }
  .brand-back .brand-name { font-size: 42px; }
  .brand-back .brand-url { font-size: 13px; margin-top: 6px; }
</style>
</head>
<body>

<section class="card card--front" aria-label="Business card front">
  <div class="brand-front">
    <span class="brand-dot"></span>
    <div class="brand-name">Vemtra Group</div>
    <div class="brand-url">www.vemtragroup.com</div>
  </div>

  <div class="contact">
    <div class="contact__name">Marcus Ellery JR</div>
    <div class="contact__row">
      <svg class="contact__icon" viewBox="0 0 12 14" aria-hidden="true"><path d="M6 0a5 5 0 0 0-5 5c0 3.6 5 9 5 9s5-5.4 5-9a5 5 0 0 0-5-5zm0 7a2 2 0 1 1 0-4 2 2 0 0 1 0 4z"/></svg>
      <span>2450 Linden Park NW Suite 200</span>
    </div>
    <div class="contact__row contact__row--plain">Halden, GA 30412</div>
    <div class="contact__row">
      <svg class="contact__icon" viewBox="0 0 12 14" aria-hidden="true"><path d="M3 0.5 1.2 1.6C0 2.4-.2 4.6 1.4 7.8c1.7 3.3 3.9 5.7 5.6 5.6l2-1.1c.5-.3.6-.8.3-1.2L8 9.2c-.3-.4-.8-.5-1.2-.3l-1 .6C5 8.8 4.2 7.2 4 6.2l1-.6c.4-.3.5-.8.3-1.2L4.2.8C3.9.4 3.4.2 3 .5z"/></svg>
      <span>555.014.2276</span>
    </div>
    <div class="contact__row">
      <svg class="contact__icon" viewBox="0 0 12 14" aria-hidden="true"><path d="M0 4h12v7H0zM.8 4.6 6 8.2l5.2-3.6" stroke="#fff" stroke-width="0.9"/></svg>
      <span>info@vemtragroup.com</span>
    </div>
  </div>

  <div class="front-rule"></div>
</section>

<section class="card card--back" aria-label="Business card back">
  <div class="brand-back">
    <span class="brand-dot"></span>
    <div class="brand-name">Vemtra Group</div>
    <div class="brand-url">www.vemtragroup.com</div>
  </div>
</section>

</body>
</html>
```